FenderPals Personal Injury Lawyers Website (Wordpress)

We need a brand new website for our firm's new rebranding. The name of the website is www.fenderpals-example.com. Our new brand will be a group of personal injury lawyers focused on representing only victims in car wrecks. We will be distinguishing ourselves from other law firms due to the fact that other law firms represent clients involving all forms of personal injury. We will only focus on car wrecks and this needs to be reflected on the website.

I have attached the new firm logo and stationary to show the designers the kind of look we are going for in the new website. It needs to be clean, pure, and show the potential clients that we only do one thing and we do it well. That thing is car wrecks.

Some examples of websites that we like are the following:
www.qvt-example.lu - nice interface and colors. nice navigation, we really like the biography pages for the individuals attorneys
www.morvantlegal-example.com - good layout, good navigation
www.pelliardwoss-example.com - navigation bar follows the user whether the user goes up or down

We would like five separate pages -- (1) Home, (2) Client Resources, (3) Expertise / Car Wrecks, (4) Contact Us, (5) News

The Home page will be used for driving traffic and should have a call to action on the right at the top stating that we will send an ebook to anyone who gives their contact information. The ebook will explain how car wrecks work. This should also have room for youtube videos which will be added later.

The client resources will include blogs, books, and information for potential clients. It should be presented in a well developed manner which is both appealing to potential and current clients.

The expertise page will show that we only focus on car wrecks. This needs to be a recurrent theme throughout the entire website. This page will focus on car wrecks and the different aspects including damages, insurance, and investigation.

The Contact Us page will show a google map to our address and phone number. Please use generic information and we will fill in the gaps upon the selection.

News: the news page will show different articles related to past and present cases and the successes of those clients.

The overall page should be elegant and creative. Do not include courthouses, gavels or anything else related to the law. If you include these things, your design will automatically be excluded.
Updates

Please take note this design is now guaranteed. I look forward to receiving everyone's wonderful designs.

Target Market(s)

Persons involved in car wrecks

Industry/Entity Type

Legal

Coding

Coded - Design and coding required

Number of Pages Required

5+ page

Font styles to use
Serif
Sans Serif

Colors
ec1f27
ffffff
000000

Requirements
Must have
• Five pages which focus on representation of car wreck victims. The site must be clean and easy to navigate.
Nice to have
• Navigation bar should follow user up and down the page.
Should not have
• Gavels, court houses, anything related to the law. If your design has these aspects, it will automatically be rejected

```html
<!DOCTYPE html>
<html lang="en">
<head>
<meta charset="utf-8">
<title>FenderPals – Personal Injury Lawyers</title>
<link href="https://fonts.googleapis.com/css2?family=Open+Sans:wght@400;600;700&display=swap" rel="stylesheet">
<style>
:root{
  --red:#ec1f27;
  --black:#000000;
  --white:#ffffff;
  --ink:#333333;
  --muted:#777777;
  --soft:#9a9a9a;
  --line:#e3e3e3;
  --blue:#1f86cf;
  --grey-bar:#7d7d7d;
  --grey-light:#f1f1f1;
  --dark:#1f1f1f;
  --footer:#eeeeee;
}
*{box-sizing:border-box;margin:0;padding:0}
html,body{width:1200px;height:3488px;overflow:hidden}
body{font-family:'Open Sans',Arial,sans-serif;color:var(--ink);background:var(--white);font-size:13px;line-height:1.55}
.wrap{width:1000px;margin:0 auto;position:relative}
p{color:var(--muted)}

/* top bar */
.topbar{height:32px;background:var(--dark);color:#cfcfcf;font-size:11px}
.topbar .wrap{display:flex;align-items:center;height:32px;gap:14px}
.topbar span{display:flex;align-items:center;gap:6px}

/* header */
.site-header{height:72px;background:var(--white);border-bottom:1px solid var(--line)}
.site-header .wrap{display:flex;align-items:center;justify-content:space-between;height:72px}
.brand{display:flex;align-items:center;gap:10px}
.brand-mark{width:14px;height:14px;background:var(--red);display:block}
.brand-name{font-size:26px;font-weight:600;color:var(--ink);line-height:1}
.main-nav{display:flex;align-items:center;gap:4px}
.main-nav a{font-size:12px;color:var(--ink);text-decoration:none;padding:8px 14px;border-radius:2px}
.main-nav a.active{background:var(--red);color:var(--white)}
.pdf-icon{margin-left:12px}

/* hero */
.hero{height:456px;position:relative;overflow:hidden}
.hero-photo{position:absolute;inset:0;background:
  radial-gradient(ellipse 200px 300px at 860px 240px,#5b5048 0%,#3a3330 45%,transparent 75%),
  linear-gradient(90deg,#151515 0%,#2b2726 40%,#3a2e2d 65%,#1b1616 100%)}
.hero-copy{position:absolute;left:144px;top:176px;width:540px;color:var(--white)}
.hero-copy h1{font-size:30px;font-weight:600;line-height:1.2;margin-bottom:10px;white-space:nowrap}
.hero-copy p{color:#d8d8d8;font-size:12px;line-height:1.6;margin-bottom:16px;width:440px}
.btn{display:inline-block;background:var(--red);color:var(--white);font-size:12px;padding:7px 16px;border-radius:2px;text-decoration:none}
.slider-arrow{position:absolute;top:180px;width:24px;height:32px;background:var(--red);display:flex;align-items:center;justify-content:center}
.slider-arrow.prev{left:14px}.slider-arrow.next{right:14px}
.slider-dots{position:absolute;left:0;right:0;top:428px;display:flex;justify-content:center;gap:8px}
.slider-dots i{width:12px;height:12px;border-radius:50%;background:var(--white);display:block}

/* intro / features */
.intro{height:488px;padding-top:40px;text-align:center}
.intro h2{font-size:32px;font-weight:600;color:#555;line-height:1.25;width:760px;margin:0 auto 10px}
.intro .lead{font-size:12px;margin-bottom:40px}
.features{display:grid;grid-template-columns:repeat(3,1fr);row-gap:44px;column-gap:40px;text-align:left;width:940px;margin:0 auto}
.feature{display:flex;gap:18px;align-items:flex-start}
.feature-icon{flex:0 0 70px;height:70px;border-radius:50%;background:#f6f6f6;display:flex;align-items:center;justify-content:center}
.feature h3{font-size:16px;font-weight:600;color:#444;margin:6px 0 6px}
.feature p{font-size:12px;line-height:1.6}

/* about */
.about{height:432px;background:var(--blue);padding-top:50px;text-align:center;color:var(--white)}
.about h2{font-size:32px;font-weight:600;margin-bottom:6px}
.about .lead{color:#e4f1fb;font-size:12px;width:600px;margin:0 auto 30px}
.about-body{display:flex;gap:30px;text-align:left}
.about-card{width:470px;height:200px;background:var(--white);padding:18px 22px;border:6px solid #e9f3fa}
.about-card h3{font-size:13px;font-weight:400;color:#555;border-bottom:1px solid var(--line);padding-bottom:8px;margin-bottom:8px}
.about-card p{font-size:11px;line-height:1.6}
.video{width:500px;height:200px;position:relative;background:linear-gradient(135deg,#6d5a4a,#a58d74 45%,#4a3f36)}
.video-bar{position:absolute;left:0;right:0;top:0;height:30px;background:rgba(0,0,0,.55);color:var(--white);font-size:11px;display:flex;align-items:center;padding:0 10px}
.video-play{position:absolute;left:50%;top:50%;width:56px;height:38px;margin:-19px 0 0 -28px;background:rgba(0,0,0,.7);border-radius:8px;display:flex;align-items:center;justify-content:center}

/* recent works */
.works{height:680px;padding-top:60px;text-align:center}
.works h2{font-size:32px;font-weight:600;color:#555;margin-bottom:6px}
.works .lead{font-size:12px;width:620px;margin:0 auto 34px}
.works-grid{width:1040px;margin:0 auto;display:grid;grid-template-columns:repeat(5,1fr);gap:4px}
.work-tile{height:140px}
.t1{background:linear-gradient(135deg,#8b6b58,#c9a78c)}
.t2{background:linear-gradient(135deg,#3c3c3c,#8d8d8d)}
.t3{background:linear-gradient(135deg,#5a4a42,#a38a78)}
.t4{background:linear-gradient(135deg,#2c2c2c,#6a6a6a)}
.t5{background:linear-gradient(135deg,#a6998e,#dcd3ca)}
.t6{background:linear-gradient(135deg,#7b6f67,#c2b3a5)}
.t7{background:linear-gradient(135deg,#4b5560,#9aa4ac)}
.t8{background:linear-gradient(135deg,#6e4d3e,#b08b72)}
.t9{background:linear-gradient(135deg,#9a3a3a,#d2a090)}
.t10{background:linear-gradient(135deg,#515151,#a0a0a0)}

/* news & testimonials */
.news-row{height:568px;background:var(--white);padding-top:40px;border-top:1px solid var(--line)}
.news-row .wrap{display:flex;gap:40px}
.col{width:480px}
.col h2{font-size:26px;font-weight:600;color:var(--blue);margin-bottom:6px}
.col .lead{font-size:11px;margin-bottom:14px}
.view-all{color:var(--red);font-size:11px;float:right}
.acc-head{height:38px;display:flex;align-items:center;justify-content:space-between;padding:0 12px;font-size:12px;margin-bottom:6px}
.acc-head.open{background:var(--red);color:var(--white);margin-bottom:0}
.acc-head.closed{background:var(--grey-light);color:#555;border-left:4px solid var(--grey-bar)}
.acc-head .tog{width:26px;height:38px;margin-right:-12px;display:flex;align-items:center;justify-content:center;background:var(--grey-bar)}
.acc-head.open .tog{background:#b9141b}
.acc-body{display:flex;gap:14px;padding:14px 12px;border:1px solid var(--line);border-top:0;margin-bottom:6px}
.acc-thumb{flex:0 0 150px;height:96px;background:linear-gradient(135deg,#4e6a82,#a9bfcf)}
.acc-body h4{font-size:13px;font-weight:600;color:#444;margin-bottom:4px}
.acc-body p{font-size:11px;line-height:1.55}
.read-more{color:var(--red);font-size:11px;display:block;text-align:right;margin-top:4px}
.testimonial{display:flex;gap:16px;align-items:flex-start;margin-bottom:20px}
.avatar{flex:0 0 60px;height:60px;border-radius:50%;background:radial-gradient(circle at 50% 40%,#8a7466,#3d322c)}
.testimonial p{font-size:11px;line-height:1.55}
.testimonial .who{color:var(--soft);font-size:11px;margin-top:4px}
.testimonial .who b{color:#555;font-weight:600}

/* clients */
.clients{height:248px;background:linear-gradient(180deg,#2a2a2a,#141414);text-align:center;padding-top:24px;color:var(--white)}
.clients h2{font-size:30px;font-weight:600;margin-bottom:4px}
.clients .lead{color:#c9c9c9;font-size:11px;width:560px;margin:0 auto 16px}
.client-grid{display:grid;grid-template-columns:repeat(7,124px);gap:8px 10px;justify-content:center}
.client{height:42px;background:var(--white);display:flex;align-items:center;justify-content:center;gap:6px;color:#444;font-size:13px;font-weight:600}
.client i{width:10px;height:10px;background:#444;display:block;border-radius:50%}

/* cta */
.cta{height:192px;position:relative;overflow:hidden;border-bottom:1px solid var(--line)}
.cta .wrap{display:flex;gap:18px;padding-top:42px}
.cta-icon{flex:0 0 56px;height:56px;border-radius:50%;background:var(--dark);display:flex;align-items:center;justify-content:center}
.cta h3{font-size:19px;font-weight:600;color:#333;margin-bottom:2px}
.cta p{font-size:11px;width:520px;margin-bottom:10px}
.cta-photo{position:absolute;right:0;top:0;width:420px;height:192px;background:linear-gradient(90deg,#ffffff 0%,rgba(224,214,204,.6) 35%,#cbbcae 100%)}

/* footer */
.site-footer{height:272px;background:var(--footer);padding-top:34px}
.footer-cols{display:grid;grid-template-columns:repeat(4,1fr);gap:30px}
.footer-cols h4{font-size:15px;font-weight:600;color:#333;margin-bottom:10px;padding-bottom:6px;border-bottom:1px solid #d6d6d6}
.footer-cols li{list-style:none;font-size:11px;color:var(--muted);line-height:2}

/* bottom bar */
.bottom-bar{height:48px;background:var(--dark);color:#bdbdbd;font-size:11px;border-top:4px solid var(--red)}
.bottom-bar .wrap{display:flex;justify-content:space-between;align-items:center;height:44px}
.bottom-bar nav{display:flex;gap:18px}
</style>
</head>
<body>

<div class="topbar">
  <div class="wrap">
    <span><svg width="11" height="11" viewBox="0 0 24 24"><path fill="#cfcfcf" d="M6.6 10.8a15 15 0 0 0 6.6 6.6l2.2-2.2c.3-.3.7-.4 1-.2 1.1.4 2.3.6 3.6.6.6 0 1 .4 1 1V20c0 .6-.4 1-1 1A17 17 0 0 1 3 4c0-.6.4-1 1-1h3.5c.6 0 1 .4 1 1 0 1.3.2 2.5.6 3.6.1.3 0 .7-.2 1z"/></svg>+01 555 010 2040</span>
    <span><svg width="12" height="10" viewBox="0 0 24 18"><rect x="1" y="1" width="22" height="16" fill="none" stroke="#cfcfcf" stroke-width="2"/><path d="M1 1l11 9 11-9" fill="none" stroke="#cfcfcf" stroke-width="2"/></svg>info@fenderpals-example.com</span>
  </div>
</div>

<header class="site-header">
  <div class="wrap">
    <div class="brand">
      <i class="brand-mark"></i>
      <span class="brand-name">FenderPals</span>
    </div>
    <nav class="main-nav">
      <a class="active" href="#">Home</a>
      <a href="#">Solutions ▾</a>
      <a href="#">About Us</a>
      <a href="#">News</a>
      <a href="#">Resources</a>
      <a href="#">Contact</a>
      <svg class="pdf-icon" width="24" height="30" viewBox="0 0 24 30"><path d="M2 1h14l6 6v22H2z" fill="none" stroke="#ec1f27" stroke-width="2"/><path d="M16 1v6h6" fill="none" stroke="#ec1f27" stroke-width="2"/><path d="M6 22c4-3 7-8 6-12-1 4 2 9 6 10-4-1-9 0-12 2z" fill="none" stroke="#ec1f27" stroke-width="1.5"/></svg>
    </nav>
  </div>
</header>

<section class="hero">
  <div class="hero-photo" role="img" aria-label="Lawyer in a dark suit standing in front of a blurred city street at night"></div>
  <div class="hero-copy">
    <h1>Lorem Ipsum Dolor Sit Amet</h1>
    <p>Lorem ipsum dolor sit amet, consectetur adipiscing elit, sed do eiusmod tempor incididunt ut labore et dolore magna aliqua. Ut enim ad minim veniam, quis nostrud exercitation ullamco laboris nisi ut aliquip ex ea commodo consequat.</p>
    <a class="btn" href="#">Read More</a>
  </div>
  <div class="slider-arrow prev"><svg width="8" height="12" viewBox="0 0 8 12"><path d="M7 1L2 6l5 5" fill="none" stroke="#fff" stroke-width="2"/></svg></div>
  <div class="slider-arrow next"><svg width="8" height="12" viewBox="0 0 8 12"><path d="M1 1l5 5-5 5" fill="none" stroke="#fff" stroke-width="2"/></svg></div>
  <div class="slider-dots"><i></i><i></i><i></i></div>
</section>

<section class="intro">
  <h2>A group of personal injury lawyers focused on representing only victims in car wrecks</h2>
  <p class="lead">Lorem ipsum dolor sit amet, consectetur adipiscing elit, sed do eiusmod tempor incididunt ut labore et dolore magna aliqua. Ut enim ad minim veniam.</p>
  <div class="features">
    <div class="feature">
      <div class="feature-icon"><svg width="34" height="26" viewBox="0 0 34 26"><path d="M3 14l4-9h20l4 9v8h-4v3h-4v-3H11v3H7v-3H3z" fill="#ec1f27"/><circle cx="9" cy="17" r="2.2" fill="#fff"/><circle cx="25" cy="17" r="2.2" fill="#fff"/><path d="M9 7h16l2.5 6h-21z" fill="#fff"/></svg></div>
      <div><h3>Fast Solution</h3><p>Lorem ipsum dolor sit amet, consectetur adipiscing elit.</p></div>
    </div>
    <div class="feature">
      <div class="feature-icon"><svg width="32" height="28" viewBox="0 0 32 28"><path d="M4 2h24a3 3 0 0 1 3 3v13a3 3 0 0 1-3 3H14l-7 6v-6H4a3 3 0 0 1-3-3V5a3 3 0 0 1 3-3z" fill="#ec1f27"/></svg></div>
      <div><h3>Always online, 24/7</h3><p>Lorem ipsum dolor sit amet, consectetur adipiscing elit.</p></div>
    </div>
    <div class="feature">
      <div class="feature-icon"><svg width="30" height="30" viewBox="0 0 30 30"><path d="M4 12a11 11 0 0 1 20-5" fill="none" stroke="#ec1f27" stroke-width="3"/><path d="M26 3v6h-6" fill="none" stroke="#ec1f27" stroke-width="3"/><path d="M26 18a11 11 0 0 1-20 5" fill="none" stroke="#ec1f27" stroke-width="3"/><path d="M4 27v-6h6" fill="none" stroke="#ec1f27" stroke-width="3"/></svg></div>
      <div><h3>Interactive</h3><p>Lorem ipsum dolor sit amet, consectetur adipiscing elit.</p></div>
    </div>
    <div class="feature">
      <div class="feature-icon"><svg width="30" height="30" viewBox="0 0 30 30"><circle cx="15" cy="15" r="7" fill="none" stroke="#ec1f27" stroke-width="5" stroke-dasharray="3 2.5"/><circle cx="15" cy="15" r="9" fill="none" stroke="#ec1f27" stroke-width="2"/><circle cx="15" cy="15" r="3" fill="#ec1f27"/></svg></div>
      <div><h3>Integrated Expertise</h3><p>Lorem ipsum dolor sit amet, consectetur adipiscing elit.</p></div>
    </div>
    <div class="feature">
      <div class="feature-icon"><svg width="32" height="26" viewBox="0 0 32 26"><path d="M2 2v22h28" fill="none" stroke="#ec1f27" stroke-width="2.5"/><path d="M6 19l7-8 5 5 10-11" fill="none" stroke="#ec1f27" stroke-width="3"/></svg></div>
      <div><h3>Real-time Analysis</h3><p>Lorem ipsum dolor sit amet, consectetur adipiscing elit, sed do eiusmod tempor.</p></div>
    </div>
    <div class="feature">
      <div class="feature-icon"><svg width="24" height="30" viewBox="0 0 24 30"><path d="M6 13V9a6 6 0 0 1 12 0v4" fill="none" stroke="#ec1f27" stroke-width="3"/><rect x="2" y="13" width="20" height="15" rx="2" fill="#ec1f27"/><circle cx="12" cy="20" r="2" fill="#fff"/></svg></div>
      <div><h3>Trusted &amp; Secured</h3><p>Lorem ipsum dolor sit amet, consectetur adipiscing elit.</p></div>
    </div>
  </div>
</section>

<section class="about">
  <div class="wrap">
    <h2>About FenderPals</h2>
    <p class="lead">Lorem ipsum dolor sit amet, consectetur adipiscing elit, sed do eiusmod tempor incididunt ut labore et dolore magna aliqua. Ut enim ad minim veniam.</p>
    <div class="about-body">
      <div class="about-card">
        <h3>Lorem ipsum dolor sit amet</h3>
        <p>Lorem ipsum dolor sit amet, consectetur adipiscing elit, sed do eiusmod tempor incididunt ut labore et dolore magna aliqua. Ut enim ad minim veniam, quis nostrud exercitation ullamco laboris nisi ut aliquip ex ea commodo consequat. Duis aute irure dolor in reprehenderit in voluptate velit esse cillum dolore eu fugiat nulla pariatur. Excepteur sint occaecat cupidatat non proident, sunt in culpa qui officia deserunt mollit anim id est laborum. Sed ut perspiciatis unde omnis iste natus error sit voluptatem.</p>
      </div>
      <div class="video" role="img" aria-label="Video still of a meeting around a conference table">
        <div class="video-bar">Introducing our car wreck team</div>
        <div class="video-play"><svg width="16" height="18" viewBox="0 0 16 18"><path d="M1 1l14 8-14 8z" fill="#fff"/></svg></div>
      </div>
    </div>
  </div>
</section>

<section class="works">
  <h2>Recent Works</h2>
  <p class="lead">Lorem ipsum dolor sit amet, consectetur adipiscing elit, sed do eiusmod tempor incididunt ut labore et dolore magna aliqua. Ut enim ad minim veniam.</p>
  <div class="works-grid">
    <div class="work-tile t1" role="img" aria-label="Team working together at a laptop"></div>
    <div class="work-tile t2" role="img" aria-label="Hands typing on a keyboard"></div>
    <div class="work-tile t3" role="img" aria-label="Client consultation at a desk"></div>
    <div class="work-tile t4" role="img" aria-label="Person thinking at a window"></div>
    <div class="work-tile t5" role="img" aria-label="Hand holding a smartphone"></div>
    <div class="work-tile t6" role="img" aria-label="Office meeting in progress"></div>
    <div class="work-tile t7" role="img" aria-label="Laptop screen with documents"></div>
    <div class="work-tile t8" role="img" aria-label="Colleagues reviewing paperwork"></div>
    <div class="work-tile t9" role="img" aria-label="Person reading a report"></div>
    <div class="work-tile t10" role="img" aria-label="Phone call at a workstation"></div>
    <div class="work-tile t4" role="img" aria-label="Team discussion in a meeting room"></div>
    <div class="work-tile t1" role="img" aria-label="Notes on a tablet"></div>
    <div class="work-tile t7" role="img" aria-label="Workspace with monitors"></div>
    <div class="work-tile t3" role="img" aria-label="Person writing at a desk"></div>
    <div class="work-tile t6" role="img" aria-label="Group working on laptops"></div>
  </div>
</section>

<section class="news-row">
  <div class="wrap">
    <div class="col">
      <h2>Latest News &amp; Events</h2>
      <p class="lead">Lorem ipsum dolor sit amet, consectetur adipiscing elit, sed do eiusmod tempor incididunt ut labore et dolore magna. <span class="view-all">+ View all News</span></p>
      <div class="acc-head open">Heading of the Latest New 01<span class="tog"><svg width="10" height="2"><rect width="10" height="2" fill="#fff"/></svg></span></div>
      <div class="acc-body">
        <div class="acc-thumb" role="img" aria-label="Laptop and papers on a desk"></div>
        <div>
          <h4>Adipiscing elit</h4>
          <p>Lorem ipsum dolor sit amet, consectetur adipiscing elit, sed do eiusmod tempor incididunt ut labore et dolore magna aliqua. Ut enim ad minim veniam, quis nostrud.</p>
          <span class="read-more">Read more</span>
        </div>
      </div>
      <div class="acc-head closed">Heading of the Latest New 02<span class="tog"><svg width="10" height="10"><path d="M0 5h10M5 0v10" stroke="#fff" stroke-width="2"/></svg></span></div>
      <div class="acc-head closed">Heading of the Latest New 03<span class="tog"><svg width="10" height="10"><path d="M0 5h10M5 0v10" stroke="#fff" stroke-width="2"/></svg></span></div>
      <div class="acc-head closed">Heading of the Latest New 04<span class="tog"><svg width="10" height="10"><path d="M0 5h10M5 0v10" stroke="#fff" stroke-width="2"/></svg></span></div>
      <div class="acc-head closed">Heading of the Latest New 05<span class="tog"><svg width="10" height="10"><path d="M0 5h10M5 0v10" stroke="#fff" stroke-width="2"/></svg></span></div>
    </div>
    <div class="col">
      <h2>Testimonials</h2>
      <p class="lead">Lorem ipsum dolor sit amet, consectetur adipiscing elit, sed do eiusmod tempor incididunt ut labore et dolore magna aliqua. Ut enim ad minim veniam.</p>
      <div class="testimonial">
        <div class="avatar" role="img" aria-label="Client portrait"></div>
        <div><p>Lorem ipsum dolor sit amet, consectetur adipiscing elit, sed do eiusmod tempor incididunt ut labore et dolore magna aliqua.</p><p class="who"><b>Jane Ross</b> Office Manager</p></div>
      </div>
      <div class="testimonial">
        <div class="avatar" role="img" aria-label="Client portrait"></div>
        <div><p>Lorem ipsum dolor sit amet, consectetur adipiscing elit, sed do eiusmod tempor incididunt ut labore et dolore magna aliqua.</p><p class="who"><b>Mark Elden</b> Teacher</p></div>
      </div>
      <div class="testimonial">
        <div class="avatar" role="img" aria-label="Client portrait"></div>
        <div><p>Lorem ipsum dolor sit amet, consectetur adipiscing elit, sed do eiusmod tempor incididunt ut labore et dolore magna aliqua.</p><p class="who"><b>Lena Pratt</b> Nurse</p></div>
      </div>
    </div>
  </div>
</section>

<section class="clients">
  <h2>Valued Clients</h2>
  <p class="lead">Lorem ipsum dolor sit amet, consectetur adipiscing elit, sed do eiusmod tempor incididunt ut labore et dolore magna aliqua.</p>
  <div class="client-grid">
    <div class="client">Corvane</div>
    <div class="client">Norvik</div>
    <div class="client">Brightlens</div>
    <div class="client">Papeline</div>
    <div class="client">Marlow Vey</div>
    <div class="client">Valemont</div>
    <div class="client">Roadhire</div>
    <div class="client"><i></i>Tellbank</div>
    <div class="client">Ostwick Rent</div>
    <div class="client">Ulvana</div>
    <div class="client">Halden Co</div>
    <div class="client">Cleanforte</div>
    <div class="client">Kestrel Group</div>
    <div class="client">Brisant</div>
  </div>
</section>

<section class="cta">
  <div class="cta-photo" role="img" aria-label="Smiling team of advisers in an office"></div>
  <div class="wrap">
    <div class="cta-icon"><svg width="24" height="24" viewBox="0 0 24 24"><path fill="#fff" d="M6.6 10.8a15 15 0 0 0 6.6 6.6l2.2-2.2c.3-.3.7-.4 1-.2 1.1.4 2.3.6 3.6.6.6 0 1 .4 1 1V20c0 .6-.4 1-1 1A17 17 0 0 1 3 4c0-.6.4-1 1-1h3.5c.6 0 1 .4 1 1 0 1.3.2 2.5.6 3.6.1.3 0 .7-.2 1z"/></svg></div>
    <div>
      <h3>Have a question or need a custom quote?</h3>
      <p>Lorem ipsum dolor sit amet, consectetur adipiscing elit, sed do eiusmod tempor incididunt ut labore et dolore magna aliqua. Ut enim ad minim veniam, quis nostrud exercitation.</p>
      <a class="btn" href="#">Contact Details</a>
    </div>
  </div>
</section>

<footer class="site-footer">
  <div class="wrap footer-cols">
    <div><h4>COMPANY</h4><ul><li>About us</li><li>Meet the team</li><li>Copyright</li><li>Privacy policy</li><li>Contact us</li></ul></div>
    <div><h4>SUPPORT</h4><ul><li>Faq</li><li>Blog</li><li>Forum</li><li>Ticket system</li><li>Billing system</li></ul></div>
    <div><h4>LOREM IPSUM</h4><ul><li>Lorem ipsum dolor</li><li>Consectetur elit</li><li>Lorem ipsum dolor</li><li>Sed do eiusmod</li><li>Tempor incididunt</li></ul></div>
    <div><h4>OUR PARTNERS</h4><ul><li>Adipiscing elit</li><li>Eiusmod</li><li>Tempor</li><li>Labore</li><li>Dolore magna</li></ul></div>
  </div>
</footer>

<div class="bottom-bar">
  <div class="wrap">
    <span>© 2014 FenderPals All Rights Reserved.</span>
    <nav><span>Home</span><span>About us</span><span>Faq</span><span>Contact Us</span></nav>
  </div>
</div>

</body>
</html>
```